Test and Tag business card design

We are an appliance test and tag company in Brisbane Australia requiring a business card design.
I don't have a logo.
Card front: Matte black background with white font.
Card back: White background with black font colour
Examples are attached
Minimalist design
Reason: Looking for more designs with an extreme minimal feel
Industry/Entity Type
Appliance
Contact Information for Business Card
Business name: Harbor Check and Label
Description: Onsite Electrical Testing and Tagging
Licence No. 41853
Name: Greg Pellow
Mobile: 0418 526 937
Email: greg@harborcheckandlabel.com.au
Web: harborcheckandlabel.com.au
Logo Text
Harbor Check and Label
Look and feel

```html
<!DOCTYPE html>
<html lang="en">
<head>
<meta charset="utf-8">
<title>Harbor Check and Label — Business Card</title>
<link rel="stylesheet" href="https://fonts.googleapis.com/css2?family=Questrial&display=swap">
<style>
  :root {
    --stage: #3b3b3d;
    --card-dark: #1f1f21;
    --card-light: #ecebe6;
    --ink-light: #e9e9e9;
    --ink-muted: #bdbdbd;
    --ink-dark: #1b1b1b;
    --ink-grey: #6a6a6a;
    --rule: #8a8a8a;
  }
  * { margin: 0; padding: 0; box-sizing: border-box; }
  html, body {
    width: 1200px; height: 900px; overflow: hidden;
    background: var(--stage);
    font-family: "Questrial", "Century Gothic", sans-serif;
  }
  .sheet {
    width: 1200px; height: 900px;
    display: flex; flex-direction: column;
    align-items: center; justify-content: center; gap: 50px;
  }
  .card {
    position: relative;
    width: 620px; height: 354px;
    box-shadow: 0 14px 30px rgba(0,0,0,0.35);
  }
  .card--back { background: var(--card-light); color: var(--ink-dark); }
  .card--front { background: var(--card-dark); color: var(--ink-light); }

  .wordmark {
    font-size: 30px; letter-spacing: 0.5px;
    text-transform: uppercase; white-space: nowrap;
  }

  /* back */
  .card--back .wordmark {
    position: absolute; left: 0; right: 0; top: 156px;
    text-align: center; color: var(--ink-dark);
  }
  .card--back .web {
    position: absolute; right: 34px; bottom: 26px;
    font-size: 12px; color: var(--ink-grey); letter-spacing: 0.3px;
  }

  /* front */
  .card--front .wordmark {
    position: absolute; left: 28px; top: 212px;
    font-size: 23px; color: var(--ink-light);
  }
  .divider {
    position: absolute; left: 310px; top: 60px; width: 1px; height: 234px;
    background: linear-gradient(to bottom, transparent, var(--rule) 50%, transparent);
  }
  .contact {
    position: absolute; left: 340px; top: 62px;
    list-style: none; font-size: 14px; color: var(--ink-light);
  }
  .contact__name {
    font-size: 16px; letter-spacing: 1px; text-transform: uppercase;
    margin-bottom: 16px;
  }
  .contact__item {
    display: flex; align-items: center; gap: 9px;
    font-size: 12.5px; margin-bottom: 8px; color: var(--ink-muted);
  }
  .contact__item svg { width: 14px; height: 14px; flex: none; }
  .contact__desc {
    margin-top: 22px; font-size: 13px; line-height: 1.45; color: var(--ink-muted);
  }
</style>
</head>
<body>
<main class="sheet">
  <section class="card card--back" aria-label="Card back">
    <p class="wordmark">Harbor Check &amp; Label</p>
    <p class="web">www.harborcheckandlabel.com.au</p>
  </section>

  <section class="card card--front" aria-label="Card front">
    <p class="wordmark">Harbor Check &amp; Label</p>
    <div class="divider"></div>
    <ul class="contact">
      <li class="contact__name">Greg Pellow</li>
      <li class="contact__item">
        <svg viewBox="0 0 14 14" aria-hidden="true"><circle cx="7" cy="7" r="7" fill="#e9e9e9"/><path d="M4.6 3.6l1.3 1.6-.7.9c.5 1 1.3 1.8 2.3 2.3l.9-.7 1.6 1.3-.8 1.2C6.6 10 4 7.4 3.6 4.4z" fill="#1f1f21"/></svg>
        0418 526 937
      </li>
      <li class="contact__item">
        <svg viewBox="0 0 14 14" aria-hidden="true"><circle cx="7" cy="7" r="7" fill="#e9e9e9"/><rect x="3.5" y="4.5" width="7" height="5" fill="none" stroke="#1f1f21" stroke-width="1"/><path d="M3.5 4.5L7 7.3l3.5-2.8" fill="none" stroke="#1f1f21" stroke-width="1"/></svg>
        greg@harborcheckandlabel.com.au
      </li>
      <li class="contact__item">
        <svg viewBox="0 0 14 14" aria-hidden="true"><circle cx="7" cy="7" r="7" fill="#e9e9e9"/><circle cx="7" cy="7" r="3.8" fill="none" stroke="#1f1f21" stroke-width="0.9"/><ellipse cx="7" cy="7" rx="1.6" ry="3.8" fill="none" stroke="#1f1f21" stroke-width="0.9"/><path d="M3.2 7h7.6" stroke="#1f1f21" stroke-width="0.9"/></svg>
        www.harborcheckandlabel.com.au
      </li>
      <li class="contact__desc">Onsite Electrical Testing<br>and Tagging Licence No. 41853</li>
    </ul>
  </section>
</main>
</body>
</html>
```